The calm within me tour 2019

I need an improvement of my own design for a speaking tour on shame and mental health. The advertisement will be for social media. I would like someone to remove the background and do something creative and contemporary. My preference is just my head and shoulders.

Target Market(s)

Church pastors and leaders of mental health organisations

Industry/Entity Type

Mental Health

Requirements
Must have
• The same wording as original
• Delete background and replace with something that is simple but funky

```html
<!DOCTYPE html>
<html lang="en">
<head>
<meta charset="utf-8">
<title>The Calm Within Me Tour 2019</title>
<link href="https://fonts.googleapis.com/css2?family=Comfortaa:wght@400&family=Montserrat:wght@500;800&display=swap" rel="stylesheet">
<style>
  :root {
    --bg-left-top: #2e2e2e;
    --bg-left-bottom: #232323;
    --bg-right: #141414;
    --text-white: #ffffff;
    --accent-blue: #4d7dff;
    --portrait-light: #8a8a8a;
    --portrait-mid: #4a4a4a;
    --portrait-dark: #151515;
  }
  html, body {
    margin: 0;
    padding: 0;
    width: 1200px;
    height: 1200px;
    overflow: hidden;
    background: var(--bg-right);
  }
  .poster {
    position: relative;
    width: 1200px;
    height: 1200px;
    background: linear-gradient(180deg, var(--bg-left-top), var(--bg-left-bottom));
    overflow: hidden;
  }
  .poster__side-band {
    position: absolute;
    top: 0;
    right: 0;
    width: 530px;
    height: 1200px;
    background: var(--bg-right);
  }
  .poster__portrait {
    position: absolute;
    left: 610px;
    top: 170px;
    width: 590px;
    height: 1030px;
    border-radius: 46% 44% 0 0 / 30% 28% 0 0;
    background: radial-gradient(ellipse 48% 38% at 52% 30%, var(--portrait-light), var(--portrait-mid) 60%, var(--portrait-dark) 100%);
  }
  .poster__title {
    position: absolute;
    left: 0;
    top: 240px;
    width: 680px;
    text-align: center;
    color: var(--text-white);
  }
  .title__lead {
    display: block;
    font-family: "Comfortaa", sans-serif;
    font-weight: 400;
    font-size: 82px;
    line-height: 1;
    margin-bottom: 22px;
  }
  .title__main {
    display: block;
    font-family: "Montserrat", sans-serif;
    font-weight: 800;
    font-size: 80px;
    line-height: 1.18;
    letter-spacing: 1px;
  }
  .title__tour {
    display: block;
    margin-top: 28px;
    font-family: "Comfortaa", sans-serif;
    font-weight: 400;
    font-style: italic;
    font-size: 78px;
    letter-spacing: 8px;
    color: var(--accent-blue);
  }
  .poster__brand {
    position: absolute;
    left: 70px;
    top: 940px;
    display: flex;
    flex-direction: column;
    align-items: center;
    gap: 22px;
  }
  .brand__mark {
    width: 120px;
    height: 120px;
    border-radius: 50%;
    background: var(--accent-blue);
  }
  .brand__name {
    font-family: "Montserrat", sans-serif;
    font-weight: 500;
    font-size: 44px;
    color: var(--accent-blue);
    line-height: 1;
  }
</style>
</head>
<body>
  <main class="poster">
    <div class="poster__side-band"></div>
    <div class="poster__portrait" role="img" aria-label="Black and white head-and-shoulders portrait of the speaker in a dark v-neck shirt"></div>

    <h1 class="poster__title">
      <span class="title__lead">the</span>
      <span class="title__main">CALM WITHIN<br>ME</span>
      <span class="title__tour">TOUR 2019</span>
    </h1>

    <div class="poster__brand">
      <span class="brand__mark"></span>
      <span class="brand__name">ben harlow</span>
    </div>
  </main>
</body>
</html>
```